Business Card Design for Oncology Consulting Company

We need a business card design using a logo that has already been created.

Company name is: WMBHO - Guild for Tumor Projection, Therapy and Remediation

We would also like to include the following pieces of information on the business card:
Name
Title
US Address (street, city, state, zip, country)
Email address
Website address

Target Market(s)

The target customers are physicians (oncologists, pathologists) in Greece, Iran, US, etc who would refer patients to our company for a second medical opinion/genetic counseling for cancer.

Industry/Entity Type

Business

Colors

Designer to choose colors to be used in the design.

Requirements
Must have
• Must contain logo in attached file and elements described above.

```html
<!DOCTYPE html>
<html lang="en">
<head>
<meta charset="utf-8">
<title>WMBHO Business Card</title>
<link rel="stylesheet" href="https://fonts.googleapis.com/css2?family=Ubuntu:wght@400;500;700&display=swap">
<style>
  :root {
    --brand-blue: #1a6bfa;
    --card-border: #8a8a8a;
    --page-bg: #ffffff;
    --muted-grey: #8f8f8f;
    --rule-grey: #b5b5b5;
    --label-ink: #111111;
    --reverse-ink: #cfdcf7;
    --reverse-rule: #d9e3f8;
  }
  * { margin: 0; padding: 0; box-sizing: border-box; }
  html, body {
    width: 1200px;
    height: 496px;
    overflow: hidden;
    background: var(--page-bg);
    font-family: "Ubuntu", sans-serif;
  }
  .sheet { position: relative; width: 1200px; height: 496px; }

  .card {
    position: absolute;
    top: 71px;
    width: 462px;
    height: 300px;
    border: 1px solid var(--card-border);
    overflow: hidden;
  }
  .card--front { left: 101px; background: #ffffff; }
  .card--back  { left: 627px; background: var(--brand-blue); }

  .front-band {
    position: absolute;
    left: 0; right: 0; bottom: 0;
    height: 17px;
    background: var(--brand-blue);
  }

  .lockup {
    position: absolute;
    left: 31px;
    top: 118px;
    display: flex;
    align-items: flex-end;
    gap: 14px;
  }
  .wordmark {
    font-weight: 700;
    font-size: 54px;
    line-height: 1;
    letter-spacing: -0.5px;
    color: var(--brand-blue);
    white-space: nowrap;
  }
  .descriptor {
    width: 176px;
    margin-bottom: 10px;
    padding-top: 4px;
    border-top: 2px solid var(--rule-grey);
    font-size: 7.6px;
    line-height: 1.35;
    font-weight: 500;
    text-transform: uppercase;
    letter-spacing: 0.2px;
    color: var(--muted-grey);
  }

  .contact {
    position: absolute;
    left: 0; right: 0;
    text-align: center;
    color: var(--reverse-ink);
    white-space: nowrap;
  }
  .contact__name  { top: 158px; font-size: 16.5px; font-weight: 500; }
  .contact__title { top: 183px; font-size: 14.5px; font-weight: 700; }
  .contact__rule {
    position: absolute;
    left: 49px; right: 48px;
    top: 226px;
    height: 1px;
    background: var(--reverse-rule);
  }
  .contact__address { top: 236px; font-size: 12.5px; font-weight: 500; }
  .contact__web     { top: 257px; font-size: 12.5px; font-weight: 500; }
  .contact__sep { padding: 0 6px; }

  .side-label {
    position: absolute;
    top: 416px;
    width: 462px;
    text-align: center;
    font-size: 14px;
    color: var(--label-ink);
  }
  .side-label--front { left: 101px; }
  .side-label--back  { left: 627px; }
</style>
</head>
<body>
<main class="sheet">
  <section class="card card--front" aria-label="Business card, front">
    <div class="lockup">
      <div class="wordmark">WMBHO</div>
      <div class="descriptor">Guild for Tumor Projection, Therapy and Remediation</div>
    </div>
    <div class="front-band"></div>
  </section>

  <section class="card card--back" aria-label="Business card, back">
    <p class="contact contact__name">Dr. Martin Caldwell Reyes</p>
    <p class="contact contact__title">Director of Investigation Department</p>
    <div class="contact__rule"></div>
    <p class="contact contact__address">428 Harbor Street, 12th floor, Boston, MA 02110-4417 USA</p>
    <p class="contact contact__web">m.reyes@wmbho.com<span class="contact__sep">|</span>www.wmbho.com</p>
  </section>

  <p class="side-label side-label--front">wmbho - side A</p>
  <p class="side-label side-label--back">wmbho - side B</p>
</main>
</body>
</html>
```